Fun relaxed Travel Photography Business Card*

Require a fun, funky and quirky but rememberable business card for a travel photographer

Industry/Entity Type

Photographer

Contact Information for Business Card

Front Card

(my name) Tavo M.

Travel Photographer ( small under travel photographer) “self-proclaimed”

(website logo) wanderingtavo.example

(Instagram logo) @wandering_with_tavo

(Instagram logo) @wandering_with_tavo_2.0 (backup for when Instagram puts Tavo on timeout for bad behaviour)

Tel: N/A (removing the potential awkwardness of me not replying)

Email: (see above)

Back Card

Offending people since 1986

(Bottom right corner) “p.s. travelling made me fatTER”

Font styles to use
Serif

Colors

Designer to choose colors to be used in the design.

Requirements
Must have
• a camera
• a similar cartoon version of me as the "logo" see attached files, try to make as similar as possible

```html
<!DOCTYPE html>
<html lang="en">
<head>
<meta charset="utf-8">
<title>Tavo M. – Travel Photographer Business Card</title>
<link rel="stylesheet" href="https://fonts.googleapis.com/css2?family=PT+Sans:wght@400;700&display=swap">
<style>
  :root {
    --backdrop: #23322b;
    --card: #29363d;
    --accent: #e8a62a;
    --ink-light: #f2f2f2;
    --art-sun: #f2b631;
    --art-earth: #5a3a22;
  }
  * { box-sizing: border-box; margin: 0; padding: 0; }
  html, body {
    width: 1200px;
    height: 1200px;
    overflow: hidden;
    background: var(--backdrop);
    font-family: "PT Sans", Arial, sans-serif;
  }
  .stage {
    position: relative;
    width: 1200px;
    height: 1200px;
  }
  .card {
    position: absolute;
    left: 160px;
    width: 880px;
    height: 503px;
    background: var(--card);
    border-radius: 6px;
  }
  .card--front { top: 70px; }
  .card--back { top: 627px; }

  /* Front */
  .mascot-art {
    position: absolute;
    left: 700px;
    top: 26px;
    width: 150px;
    height: 220px;
    border-radius: 10px;
    background: linear-gradient(160deg, var(--art-sun) 0%, #e79a22 55%, var(--art-earth) 100%);
  }
  .identity {
    position: absolute;
    left: 58px;
    top: 92px;
    line-height: 1.1;
  }
  .identity__name {
    color: var(--accent);
    font-size: 36px;
    font-weight: 400;
    letter-spacing: 1px;
  }
  .identity__role {
    color: var(--ink-light);
    font-size: 25px;
    letter-spacing: 0.5px;
    margin-top: 4px;
  }
  .identity__note {
    color: var(--ink-light);
    font-size: 17px;
    margin-top: 2px;
  }
  .contacts {
    position: absolute;
    left: 88px;
    top: 300px;
    list-style: none;
  }
  .contacts__item {
    display: flex;
    align-items: center;
    gap: 14px;
    color: var(--ink-light);
    font-size: 17px;
    height: 32px;
  }
  .contacts__mark {
    width: 14px;
    height: 14px;
    border-radius: 50%;
    background: var(--ink-light);
    flex: none;
  }
  .rule {
    position: absolute;
    left: 88px;
    top: 410px;
    width: 720px;
    height: 3px;
    background: var(--accent);
  }

  /* Back */
  .tagline {
    position: absolute;
    left: 0;
    right: 0;
    top: 220px;
    text-align: center;
    color: var(--accent);
    font-size: 44px;
    letter-spacing: 1px;
  }
  .postscript {
    position: absolute;
    right: 48px;
    bottom: 40px;
    color: var(--accent);
    font-size: 19px;
  }
</style>
</head>
<body>
<main class="stage">
  <section class="card card--front" aria-label="Business card front">
    <div class="mascot-art" role="img" aria-label="Cartoon mascot of Tavo in sunglasses and a floral shirt holding a camera, set on a yellow map shape"></div>
    <div class="identity">
      <h1 class="identity__name">TAVO M.</h1>
      <p class="identity__role">TRAVEL PHOTOGRAPHER</p>
      <p class="identity__note">self-proclaimed</p>
    </div>
    <ul class="contacts">
      <li class="contacts__item"><span class="contacts__mark"></span>wanderingtavo.example</li>
      <li class="contacts__item"><span class="contacts__mark"></span>@wandering_with_tavo</li>
      <li class="contacts__item"><span class="contacts__mark"></span>@wandering_with_tavo_2.0</li>
    </ul>
    <div class="rule"></div>
  </section>

  <section class="card card--back" aria-label="Business card back">
    <p class="tagline">OFFENDING PEOPLE SINCE 1986</p>
    <p class="postscript">p.s. travelling made me fatTER</p>
  </section>
</main>
</body>
</html>
```